Medical Staffing Pamphlet

We are starting to staff for Medical positions for the first time, we need pamphlets to take to medical facilities to try to gain new business

Need an copy to edit, many errors.

```html
<!DOCTYPE html>
<html lang="en">
<head>
<meta charset="utf-8">
<title>Brightpath Care – Tri-fold Pamphlet</title>
<link rel="stylesheet" href="https://fonts.googleapis.com/css2?family=Montserrat:wght@400;500;600&display=swap">
<style>
  :root {
    --navy: #2c3e7c;
    --mid-blue: #4f6aa6;
    --slate: #33506b;
    --green: #7ab648;
    --dark-green: #3d8a3a;
    --pale-green: #cfe0b8;
    --pale-gray: #dfe3ec;
    --sky: #9cc3e6;
    --white: #ffffff;
    --backdrop: #ececec;
    --body-light: #d7deef;
  }
  * { box-sizing: border-box; margin: 0; padding: 0; }
  html, body { width: 1200px; height: 881px; overflow: hidden; background: var(--backdrop); }
  body { position: relative; font-family: "Montserrat", sans-serif; }

  .spread { position: absolute; top: 220px; width: 570px; height: 440px; overflow: hidden; }
  .spread--outside { left: 20px; }
  .spread--inside { left: 610px; }
  .spread__art { position: absolute; inset: 0; width: 570px; height: 440px; }

  .panel { position: absolute; top: 0; width: 190px; height: 440px; }
  .panel--1 { left: 0; }
  .panel--2 { left: 190px; }
  .panel--3 { left: 380px; }
  .abs { position: absolute; }
  .center { left: 0; width: 190px; text-align: center; }

  .tagline { color: var(--green); font-size: 10.5px; line-height: 23px; font-weight: 400; }
  .tagline--front { font-size: 10px; line-height: 19.5px; }

  .brand-name { font-family: "Montserrat", sans-serif; font-weight: 600; letter-spacing: 0.2px; }
  .brand-name--back { top: 250px; font-size: 15px; line-height: 20px; color: var(--navy); }
  .brand-name--front { top: 180px; font-size: 24px; line-height: 30px; color: var(--white); }
  .brand-name--services { top: 360px; font-size: 14px; line-height: 18px; color: var(--white); }

  .boxed-heading {
    position: absolute; border: 1px solid currentColor;
    font-weight: 600; text-align: center; letter-spacing: 0.6px;
  }
  .contact-heading { top: 333px; left: 45px; width: 100px; height: 25px; line-height: 23px; font-size: 10.5px; color: var(--navy); }
  .contact-lines { top: 367px; font-size: 6.4px; line-height: 12.4px; color: var(--navy); }

  .section-heading { color: var(--green); font-size: 10.5px; height: 25px; line-height: 23px; }
  .about-heading { top: 282px; left: 37px; width: 122px; }
  .about-copy { top: 318px; left: 18px; width: 154px; text-align: center; color: var(--body-light); font-size: 6.2px; line-height: 11.5px; }

  .promise { top: 297px; left: 20px; width: 170px; text-align: center; color: var(--navy); font-size: 11.5px; line-height: 18.8px; }

  .services-heading { top: 32px; left: 33px; width: 122px; }
  .service-group { left: 0; width: 190px; text-align: center; color: var(--body-light); font-size: 6.6px; letter-spacing: 2.4px; font-weight: 500; }
  .service-list { list-style: none; color: var(--white); font-size: 6.4px; line-height: 13px; }
  .service-list li::before { content: "›"; color: var(--green); margin-right: 3px; }
  .service-list--admin { top: 97px; left: 44px; }
  .service-list--clinical { top: 253px; left: 47px; }
</style>
</head>
<body>

<!-- Outside spread: back flap, back cover, front cover -->
<section class="spread spread--outside">
  <svg class="spread__art" viewBox="0 0 570 440" aria-hidden="true">
    <rect width="570" height="440" fill="var(--navy)"/>
    <polygon points="0,0 150,0 0,150" fill="var(--slate)" opacity="0.85"/>
    <polygon points="30,440 190,280 190,440" fill="var(--mid-blue)" opacity="0.8"/>
    <rect x="0" y="0" width="6" height="145" fill="var(--green)"/>
    <rect x="75" y="432" width="40" height="8" fill="var(--sky)"/>
    <rect x="190" y="150" width="190" height="290" fill="var(--pale-gray)"/>
    <polygon points="190,150 300,150 190,260" fill="var(--mid-blue)" opacity="0.28"/>
    <polygon points="222,440 380,282 380,440" fill="var(--pale-green)"/>
    <polygon points="268,440 380,328 380,356 296,440" fill="var(--white)" opacity="0.55"/>
    <rect x="240" y="431" width="88" height="9" fill="var(--dark-green)"/>
    <polygon points="380,330 570,140 570,250 380,440" fill="var(--slate)" opacity="0.75"/>
    <rect x="431" y="0" width="86" height="10" fill="var(--sky)"/>
    <rect x="561" y="321" width="9" height="119" fill="var(--green)"/>
  </svg>

  <div class="panel panel--1">
    <svg class="abs" style="left:78px;top:104px" width="34" height="28" viewBox="0 0 34 28" aria-hidden="true">
      <g fill="none" stroke="var(--green)" stroke-width="1.4" stroke-linecap="round">
        <line x1="17" y1="2" x2="17" y2="27"/>
        <path d="M17 6 C11 3 6 4 2 2 M17 6 C23 3 28 4 32 2 M16 9 C11 7 7 8 4 6 M18 9 C23 7 27 8 30 6"/>
        <path d="M14 12 C20 14 20 16 14 18 C20 20 20 22 15 24"/>
      </g>
    </svg>
    <svg class="abs" style="left:0;top:172px" width="38" height="16" viewBox="0 0 38 16" aria-hidden="true">
      <g fill="var(--green)" opacity="0.6">
        <polygon points="0,0 7,0 14,8 7,16 0,16 7,8"/>
        <polygon points="12,0 19,0 26,8 19,16 12,16 19,8"/>
        <polygon points="24,0 31,0 38,8 31,16 24,16 31,8"/>
      </g>
    </svg>
    <p class="abs center tagline" style="top:169px">Our medical<br>staffing<br>specialist will<br>provide you<br>quality<br>employees</p>
  </div>

  <div class="panel panel--2">
    <div class="abs" style="left:0;top:0;width:190px;height:150px;background:linear-gradient(160deg,#4a5468 0%,#8a7060 45%,#3a4150 100%)" role="img" aria-label="Photo of a hand writing notes with a pen at a desk"></div>
    <h2 class="abs center brand-name brand-name--back">Brightpath Care</h2>
    <div class="boxed-heading contact-heading">CONTACT US</div>
    <p class="abs center contact-lines">455 Maple Crest Ave.<br>Fairview, Ohio 43210<br>555-014-2290<br>brightpathcare.com</p>
  </div>

  <div class="panel panel--3">
    <h1 class="abs center brand-name brand-name--front">Brightpath<br>Care</h1>
    <p class="abs center tagline tagline--front" style="top:316px">Providing<br>high quality<br>healthcare<br>professionals</p>
  </div>
</section>

<!-- Inside spread: who we are, promise, services -->
<section class="spread spread--inside">
  <svg class="spread__art" viewBox="0 0 570 440" aria-hidden="true">
    <rect width="570" height="440" fill="var(--navy)"/>
    <polygon points="0,440 0,330 110,440" fill="var(--mid-blue)" opacity="0.5"/>
    <polygon points="60,440 190,310 190,440" fill="var(--mid-blue)" opacity="0.55"/>
    <rect x="190" y="255" width="190" height="185" fill="var(--pale-gray)"/>
    <polygon points="218,440 380,278 380,440" fill="var(--pale-green)"/>
    <polygon points="262,440 380,322 380,350 290,440" fill="var(--white)" opacity="0.55"/>
    <rect x="240" y="426" width="87" height="14" fill="var(--navy)"/>
    <polygon points="380,230 570,40 570,150 380,340" fill="var(--slate)" opacity="0.7"/>
    <polygon points="380,120 500,0 570,0 380,190" fill="var(--mid-blue)" opacity="0.35"/>
    <rect x="560" y="0" width="8" height="156" fill="var(--green)"/>
    <rect x="560" y="400" width="10" height="40" fill="var(--sky)"/>
  </svg>

  <div class="abs" style="left:0;top:0;width:380px;height:255px;background:linear-gradient(120deg,#6fa9c8 0%,#e9eef2 40%,#f4f6f8 70%,#aebfd6 100%)" role="img" aria-label="Photo of a team of smiling medical professionals in white coats with stethoscopes"></div>
  <div class="abs" style="left:37px;top:0;width:121px;height:6px;background:var(--green)"></div>

  <div class="panel panel--1">
    <h2 class="boxed-heading section-heading about-heading">WHO WE ARE</h2>
    <p class="abs about-copy">Brightpath Care is the largest locally owned recruiting company in the Tri-State. We began building staffing partnerships are the foundation of our success. We provide customized staffing solutions for the many industries we service, including medical.</p>
    <svg class="abs" style="left:88px;top:413px" width="14" height="14" viewBox="0 0 14 14" aria-hidden="true">
      <g fill="none" stroke="var(--green)" stroke-width="1.2"><circle cx="5" cy="5" r="4"/><circle cx="9" cy="9" r="4"/></g>
    </svg>
  </div>

  <div class="panel panel--2">
    <svg class="abs" style="left:0;top:292px" width="44" height="18" viewBox="0 0 38 16" aria-hidden="true">
      <g fill="var(--green)">
        <polygon points="0,0 7,0 14,8 7,16 0,16 7,8"/>
        <polygon points="12,0 19,0 26,8 19,16 12,16 19,8"/>
        <polygon points="24,0 31,0 38,8 31,16 24,16 31,8"/>
      </g>
    </svg>
    <p class="abs promise">Put your trust<br>in us, and we<br>will take care of<br>your medical<br>staffing needs.</p>
  </div>

  <div class="panel panel--3">
    <h2 class="boxed-heading section-heading services-heading">OUR SERVICES</h2>
    <h3 class="abs service-group" style="top:76px">ADMINISTRATIVE</h3>
    <ul class="abs service-list service-list--admin">
      <li>Billing Specialists</li>
      <li>Coding Specialists</li>
      <li>Medical Records</li>
      <li>Office Managers</li>
      <li>Receptionists</li>
    </ul>
    <svg class="abs" style="left:80px;top:174px" width="32" height="43" viewBox="0 0 32 43" aria-hidden="true">
      <g fill="none" stroke="var(--green)" stroke-width="1.5" stroke-linejoin="round">
        <rect x="2" y="5" width="28" height="36" rx="2"/>
        <rect x="10" y="1" width="12" height="7" rx="1.5"/>
        <line x1="12" y1="15" x2="25" y2="15"/><line x1="12" y1="20" x2="25" y2="20"/><line x1="12" y1="25" x2="25" y2="25"/>
        <line x1="7" y1="15" x2="8" y2="15"/><line x1="7" y1="20" x2="8" y2="20"/><line x1="7" y1="25" x2="8" y2="25"/>
        <polyline points="6,33 11,33 13,29 16,36 19,30 21,33 26,33"/>
      </g>
    </svg>
    <h3 class="abs service-group" style="top:232px">CLINICAL</h3>
    <ul class="abs service-list service-list--clinical">
      <li>Certified Medical Assistants</li>
      <li>Registered Medical Assistants</li>
      <li>Certified Nursing Assistants</li>
      <li>Phlebotomists</li>
    </ul>
    <p class="abs center brand-name brand-name--services">Brightpath Care</p>
  </div>
</section>

</body>
</html>
```